Presentation of Business Project of Implementing CRM for a car Detailing Company

We need a professional PowerPoint presentation template (5 slides) for a business presentation about implementing a CRM system at Vantrel Detailing, a premium automotive detailing company in South Africa.
About the Company:
Vantrel Detailing specializes in high-end car detailing, paint protection, leather repair, and classic car restoration. They're a premium service provider looking to modernize their customer management through digital transformation.
What We Need:
A visually impressive presentation template with 5 key slide designs that we can duplicate and reuse across our full presentation. The presentation will show how a ChatLoom-integrated CRM system can help the business grow from 60% to 80% customer retention, free up the owner's time, and enable expansion.
The 5 Slides:

Title slide - Space for project title + 5 team member names (impactful opening)
Content slide - Standard layout with bullet points (we'll duplicate this for 10+ slides)
Large data table - For vendor comparisons (4 rows × 10 columns)
Financial charts - 3 side-by-side scenario comparisons with bar/column charts
Simple table - For cost breakdowns (2-3 columns)

Design Style:
Modern, polished, and eye-catching. Should look professional but capture attention - think sleek automotive industry meets premium business consulting. Bold use of car detailing/workshop imagery as backgrounds where appropriate. Contemporary color scheme. Clean layouts that make data easy to read but NOT boring.

Images:
We will provide a link to high-quality car detailing and workshop images that you can integrate into the design (backgrounds, accents, visual interest).

https://www.filebarrow.example/drive/7kqPz2LmXr9TsWd4Hn3BY-uJE#VantrelDetailing

Link contain image of company actual work and logo of the company. The idea is to use their images.

Important:
All tables and charts should be editable so we can add our own data. Slides should be easy to duplicate and modify.

Deliverables:
5 PowerPoint slides (.pptx) - fully editable
Google Slides version
Fonts/colors consistent throughout

```html
<!DOCTYPE html>
<html lang="en">
<head>
<meta charset="utf-8">
<title>Vantrel Detailing – CRM Presentation Template</title>
<link href="https://fonts.googleapis.com/css2?family=Arimo:wght@400;700&display=swap" rel="stylesheet">
<style>
:root{
  --page:#d9d6d7;
  --red:#e3242b;
  --ink:#1c1c1e;
  --panel-top:#2d2d30;
  --panel-bottom:#1b1b1d;
  --white:#ffffff;
  --muted:#b9b9bc;
  --glass:rgba(120,120,125,.45);
  --row:rgba(255,255,255,.88);
  --row-alt:rgba(236,236,238,.88);
}
*{box-sizing:border-box;margin:0;padding:0}
html,body{width:1186px;height:1200px;overflow:hidden}
body{background:var(--page);font-family:"Arimo",Arial,sans-serif;position:relative;color:var(--white)}
.slide{position:absolute;width:327px;height:184px;overflow:hidden;background:linear-gradient(160deg,var(--panel-top),var(--panel-bottom))}
.photo{position:absolute}
.title{position:absolute;left:25px;font-size:17px;font-weight:400;line-height:1.05;color:var(--white);white-space:nowrap}
.title em,.accent{color:var(--red);font-style:normal}
.brand{position:absolute;display:flex;align-items:center;gap:2px;font-size:4px;color:var(--white);white-space:nowrap}
.brand::before{content:"";width:4px;height:4px;background:var(--red)}
.lede{position:absolute;left:25px;width:115px;font-size:3.6px;line-height:1.7;color:var(--muted);text-align:justify}
.footer{position:absolute;left:22px;right:22px;top:165px;border-top:.5px solid rgba(227,36,43,.55);padding-top:2px;display:flex;justify-content:space-between;font-size:3.6px;color:var(--muted)}
.page-no{position:absolute;left:24px;top:168px;font-size:4.5px;color:#6d6d70}
.tag{display:inline-block;background:var(--red);color:var(--white);font-size:4px;width:13px;height:6px;line-height:6px;text-align:center;margin-right:7px;transform:skewX(-12deg)}
.list{position:absolute;list-style:none;font-size:5px;color:var(--white)}
.list li{display:flex;align-items:center;white-space:nowrap}
.names{font-size:7px}
.names .tag{width:14px;height:7px;line-height:7px;font-size:4.5px;margin-right:7px}
.glass{position:absolute;background:var(--glass);border-radius:4px;padding:6px 7px;font-size:3.6px;line-height:1.75;color:#eee}
.data{position:absolute;border-collapse:collapse;font-size:3.8px;color:var(--ink)}
.data th{background:var(--red);color:var(--white);font-weight:700;height:11px;border-right:.5px solid rgba(255,255,255,.5)}
.data td{height:11px;text-align:center;background:var(--row);border-bottom:.5px solid #ccc}
.data tr:nth-child(even) td{background:var(--row-alt)}
.data td:first-child{text-align:left;font-weight:700;padding-left:3px}
.goal h4{font-size:3.6px;font-weight:700;color:var(--white);display:flex;align-items:center;gap:2px}
.goal h4::before{content:"";width:2px;height:2px;background:var(--red)}
.goal p{font-size:2.6px;line-height:1.5;color:#9d9da0;margin:1px 0 0 4px}
.goal{margin-bottom:9px}
.icon-tile{position:absolute;left:165px;width:17px;height:17px;background:var(--red);display:flex;align-items:center;justify-content:center}
.contact-label{position:absolute;left:25px;font-size:4.5px;color:var(--red)}
.social{position:absolute;top:148px;width:5px;height:5px;border-radius:50%;background:var(--red)}
.section-heading{position:absolute;left:67px;top:903px;font-size:25px;font-weight:400;color:#111}
</style>
</head>
<body>

<!-- Title slide -->
<section class="slide" style="left:63px;top:53px">
  <div class="photo" role="img" aria-label="Red sports car front three-quarter view in a dark studio" style="left:130px;top:0;width:197px;height:184px;background:radial-gradient(ellipse at 60% 45%,#b3161c 0,#6e1216 30%,#2a2a2c 62%,#1c1c1e 100%)"></div>
  <div class="brand" style="left:22px;top:44px;font-size:5px">Vantrel Detailing</div>
  <h1 class="title" style="top:56px;font-size:21px">Automotive<br>Detailing,<br><span class="accent">CRM System</span></h1>
  <ul class="list names" style="left:20px;top:126px">
    <li style="height:17px"><span class="tag">01</span>Insert Name</li>
    <li style="height:17px"><span class="tag">02</span>Insert Name</li>
    <li style="height:17px"><span class="tag">03</span>Insert Name</li>
  </ul>
  <ul class="list names" style="left:120px;top:143px">
    <li style="height:17px"><span class="tag">04</span>Insert Name</li>
    <li style="height:17px"><span class="tag">05</span>Insert Name</li>
  </ul>
</section>

<!-- Contents slide -->
<section class="slide" style="left:428px;top:53px">
  <div class="photo" role="img" aria-label="Detailer applying protective film to a silver car headlight in a workshop" style="left:150px;top:0;width:177px;height:184px;clip-path:polygon(30% 0,100% 0,100% 100%,0 100%);background:linear-gradient(135deg,#4a4c50,#a9acb1 45%,#5b5d61 70%,#1f2022)"></div>
  <div class="brand" style="left:25px;top:28px">Vantrel Detailing</div>
  <h2 class="title accent" style="top:45px">Contents</h2>
  <ul class="list" style="left:25px;top:74px">
    <li style="height:17px"><span class="tag">01</span>Goals &amp; Objectives</li>
    <li style="height:17px"><span class="tag">02</span>Vendor Comparison</li>
    <li style="height:17px"><span class="tag">03</span>Scenario Comparison</li>
    <li style="height:17px"><span class="tag">04</span>Cost Breakdown</li>
    <li style="height:17px"><span class="tag">05</span>Contact Us</li>
  </ul>
  <div class="page-no" style="top:166px">02</div>
</section>

<!-- Goals & Objectives slide -->
<section class="slide" style="left:790px;top:53px">
  <div class="photo" role="img" aria-label="Black and red quilted sports seat interior" style="inset:0;background:radial-gradient(ellipse at 25% 60%,#5e1a1c 0,#2e2426 40%,#1c1c1e 80%)"></div>
  <div class="brand" style="left:282px;top:18px">Vantrel Detailing</div>
  <h2 class="title" style="top:32px">Goals &amp; <em>Objectives</em></h2>
  <div class="glass" style="left:24px;top:58px;width:83px;height:83px">Lorem ipsum color sit amet, consectetuer adipiscing elit, sed diam nonummy nibh zzril delenit augue duis dolore te feugait nulla facilisi. Lorem ipsum color sit amet, cons ectetuer ullamcorper suscipit lobortis nisl ut aliquip ex ea commodo consequat.</div>
  <div class="icon-tile" style="top:58px"><svg width="9" height="9" viewBox="0 0 10 10"><path d="M1 9h8M2 8V6M4 8V4M6 8V5M8 8V2M1 5l3-2 2 1 3-3" stroke="#fff" stroke-width=".8" fill="none"/></svg></div>
  <div class="icon-tile" style="top:80px"><svg width="9" height="9" viewBox="0 0 10 10"><rect x="2" y="1" width="5" height="8" stroke="#fff" stroke-width=".8" fill="none"/><circle cx="7.5" cy="7" r="1.8" stroke="#fff" stroke-width=".8" fill="var(--red)"/></svg></div>
  <div class="icon-tile" style="top:102px"><svg width="9" height="9" viewBox="0 0 10 10"><path d="M8.5 5a3.5 3.5 0 1 1-1-2.5M8 1v2H6" stroke="#fff" stroke-width=".8" fill="none"/></svg></div>
  <div class="icon-tile" style="top:124px"><svg width="9" height="9" viewBox="0 0 10 10"><circle cx="5" cy="5" r="3.8" stroke="#fff" stroke-width=".8" fill="none" stroke-dasharray="18 4"/><path d="M5 2.8v4.4M6.2 3.8H4.5a.8.8 0 0 0 0 1.6h1a.8.8 0 0 1 0 1.6H3.8" stroke="#fff" stroke-width=".6" fill="none"/></svg></div>
  <div style="position:absolute;left:195px;top:58px;width:110px">
    <div class="goal"><h4>Revenue Growth</h4><p>Grow repeat bookings and lift monthly revenue through loyal returning clients.</p></div>
    <div class="goal"><h4>Profit Margins</h4><p>Cut admin hours and missed follow-ups so each job keeps more margin.</p></div>
    <div class="goal"><h4>Sustainability</h4><p>Build steady processes the team can run without the owner on site.</p></div>
    <div class="goal"><h4>Return On Investment</h4><p>Recover the system cost within the first year of retained customers.</p></div>
  </div>
  <div class="footer"><span>Automotive Detailing, <span class="accent">CRM System</span></span><span>03</span></div>
</section>

<!-- Vendor Comparison slide -->
<section class="slide" style="left:63px;top:254px">
  <div class="photo" role="img" aria-label="Close-up of a silver engine cover on a sports car" style="left:150px;top:0;width:177px;height:184px;clip-path:polygon(28% 0,100% 0,100% 100%,0 100%);background:linear-gradient(140deg,#6d6e71,#b7b8bb 40%,#5c5d60 75%,#2a2a2c)"></div>
  <div class="brand" style="left:290px;top:18px">Vantrel Detailing</div>
  <h2 class="title" style="top:32px">Vendor <em>Comparison</em></h2>
  <p class="lede" style="top:60px;width:108px">Lorem ipsum dolor sit amet, consectetur adipiscing elit sed do eiusmod tempor incididunt ut labore et dolore magna aliqua. Ut enim ad minim veniam</p>
  <table class="data" style="left:25px;top:96px;width:282px">
    <tr><th></th><th>Vendor 1</th><th>Vendor 2</th><th>Vendor 3</th><th>Vendor 4</th><th>Vendor 5</th><th>Vendor 6</th><th>Vendor 7</th><th>Vendor 8</th><th>Vendor 9</th><th>Vendor 10</th></tr>
    <tr><td>Item 1</td><td>11</td><td>6</td><td>8</td><td>4</td><td>7</td><td>5</td><td>14</td><td>16</td><td>8</td><td>10</td></tr>
    <tr><td>Item 2</td><td>15</td><td>12</td><td>15</td><td>8</td><td>12</td><td>11</td><td>15</td><td>10</td><td>15</td><td>7</td></tr>
    <tr><td>Item 3</td><td>9</td><td>6</td><td>14</td><td>12</td><td>9</td><td>15</td><td>3</td><td>12</td><td>14</td><td>9</td></tr>
    <tr><td>Item 4</td><td>14</td><td>18</td><td>20</td><td>12</td><td>10</td><td>7</td><td>11</td><td>14</td><td>20</td><td>16</td></tr>
  </table>
  <div class="footer"><span>Automotive Detailing, <span class="accent">CRM System</span></span><span>04</span></div>
</section>

<!-- Scenario Comparison slide -->
<section class="slide" style="left:427px;top:254px">
  <div class="photo" role="img" aria-label="Dark sports seats with red stitching" style="inset:0;background:radial-gradient(ellipse at 30% 55%,#4a3a3c 0,#2b2628 40%,#1a1a1c 85%)"></div>
  <div class="brand" style="left:285px;top:18px">Vantrel Detailing</div>
  <h2 class="title" style="top:32px">Scenario <em>Comparison</em></h2>
  <div class="glass" style="left:24px;top:58px;width:82px;height:82px">Lorem ipsum dolor sit amet, consectetuer adipiscing elit, sed diam nonummy nibh zzril delenit augue duis dolore te feugait nulla facilisi. Lorem ipsum dolor sit amet, cons ectetuer ullamcorper suscipit lobortis nisl ut aliquip ex ea commodo consequat.</div>
  <svg style="position:absolute;left:130px;top:58px" width="170" height="100" viewBox="0 0 170 100">
    <g stroke="rgba(255,255,255,.12)" stroke-width=".4">
      <line x1="5" y1="10" x2="165" y2="10"/><line x1="5" y1="30" x2="165" y2="30"/><line x1="5" y1="50" x2="165" y2="50"/><line x1="5" y1="70" x2="165" y2="70"/><line x1="5" y1="87" x2="165" y2="87"/>
    </g>
    <g>
      <rect x="20" y="27" width="4" height="60" fill="#9a9a9d"/><rect x="25" y="52" width="4" height="35" fill="var(--red)"/><rect x="30" y="57" width="4" height="30" fill="#fff"/>
      <rect x="55" y="55" width="4" height="32" fill="#9a9a9d"/><rect x="60" y="22" width="4" height="65" fill="var(--red)"/><rect x="65" y="57" width="4" height="30" fill="#fff"/>
      <rect x="90" y="35" width="4" height="52" fill="#9a9a9d"/><rect x="95" y="60" width="4" height="27" fill="var(--red)"/><rect x="100" y="42" width="4" height="45" fill="#fff"/>
      <rect x="125" y="21" width="4" height="66" fill="#9a9a9d"/><rect x="130" y="59" width="4" height="28" fill="var(--red)"/><rect x="135" y="12" width="4" height="75" fill="#fff"/>
    </g>
    <g font-size="2.6" fill="#bbb" font-family="Arimo,Arial,sans-serif" text-anchor="middle">
      <text x="27" y="92">Vendor 1</text><text x="62" y="92">Vendor 2</text><text x="97" y="92">Vendor 3</text><text x="132" y="92">Vendor 4</text>
    </g>
    <g font-size="2.4" fill="#bbb" font-family="Arimo,Arial,sans-serif">
      <rect x="62" y="95" width="2" height="2" fill="#9a9a9d"/><text x="65" y="97">Item 1</text>
      <rect x="74" y="95" width="2" height="2" fill="var(--red)"/><text x="77" y="97">Item 2</text>
      <rect x="86" y="95" width="2" height="2" fill="#fff"/><text x="89" y="97">Item 3</text>
    </g>
  </svg>
  <div class="footer"><span>Automotive Detailing, <span class="accent">CRM System</span></span><span>05</span></div>
</section>

<!-- Cost Breakdown slide -->
<section class="slide" style="left:790px;top:254px">
  <div class="photo" role="img" aria-label="Luxury car interior with red and black leather and steering wheel" style="left:140px;top:0;width:187px;height:184px;clip-path:polygon(25% 0,100% 0,100% 100%,0 100%);background:radial-gradient(ellipse at 55% 60%,#7a1c20 0,#3a2a2c 40%,#222224 80%)"></div>
  <div class="brand" style="left:285px;top:18px">Vantrel Detailing</div>
  <h2 class="title" style="top:32px">Cost <em>Breakdown</em></h2>
  <p class="lede" style="top:60px;width:112px">Lorem ipsum dolor sit amet, consectetur adipiscing elit sed do eiusmod tempor incididunt ut labore et dolore magna aliqua. Ut enim ad minim veniam</p>
  <table class="data" style="left:26px;top:98px;width:193px">
    <tr><th></th><th>Vendor 1</th><th>Vendor 2</th><th>Vendor 3</th></tr>
    <tr><td>Item 1</td><td>11</td><td>6</td><td>8</td></tr>
    <tr><td>Item 2</td><td>15</td><td>12</td><td>15</td></tr>
    <tr><td>Item 3</td><td>9</td><td>6</td><td>14</td></tr>
    <tr><td>Item 4</td><td>14</td><td>18</td><td>20</td></tr>
  </table>
  <div class="footer"><span>Automotive Detailing, <span class="accent">CRM System</span></span><span>06</span></div>
</section>

<!-- Portfolio slide -->
<section class="slide" style="left:63px;top:454px">
  <svg style="position:absolute;left:0;top:0" width="327" height="184" viewBox="0 0 327 184" role="img" aria-label="Hexagon collage of detailed cars: red coupe, wheel with yellow caliper, dark rear light bar, black interior">
    <defs>
      <linearGradient id="pRed" x1="0" y1="0" x2="1" y2="1"><stop offset="0" stop-color="#3a3d44"/><stop offset=".5" stop-color="#b3181e"/><stop offset="1" stop-color="#2a2b2e"/></linearGradient>
      <linearGradient id="pDark" x1="0" y1="0" x2="1" y2="1"><stop offset="0" stop-color="#55575c"/><stop offset="1" stop-color="#1d1d20"/></linearGradient>
      <linearGradient id="pRear" x1="0" y1="0" x2="0" y2="1"><stop offset="0" stop-color="#4a4b50"/><stop offset=".55" stop-color="#2a2a2d"/><stop offset=".6" stop-color="#a3161c"/><stop offset="1" stop-color="#1b1b1d"/></linearGradient>
    </defs>
    <polygon points="195,3 250,3 273,45 250,87 195,87 172,45" fill="url(#pRed)"/>
    <polygon points="259,0 327,0 327,40 282,40" fill="url(#pDark)"/>
    <polygon points="260,48 327,48 327,135 272,135 252,92 282,48" fill="url(#pDark)"/>
    <polygon points="195,93 250,93 273,135 250,184 195,184 172,135" fill="url(#pRear)"/>
    <polygon points="278,142 327,142 327,184 256,184" fill="url(#pDark)"/>
  </svg>
  <div class="brand" style="left:25px;top:28px">Vantrel Detailing</div>
  <h2 class="title" style="top:45px">Our <em>Portfolio</em></h2>
  <ul class="list" style="left:24px;top:72px">
    <li style="height:14.5px"><span class="tag">01</span>Aurelle Coupe</li>
    <li style="height:14.5px"><span class="tag">02</span>Veyra Blue-Purple</li>
    <li style="height:14.5px"><span class="tag">03</span>Veyra Sport White</li>
    <li style="height:14.5px"><span class="tag">04</span>Halden Wagon</li>
    <li style="height:14.5px"><span class="tag">05</span>Marzano - Velo</li>
    <li style="height:14.5px"><span class="tag">06</span>Keller Nova White</li>
  </ul>
  <div class="footer" style="right:160px"><span></span><span></span></div>
  <div class="page-no">07</div>
</section>

<!-- Contact slide -->
<section class="slide" style="left:430px;top:454px">
  <svg style="position:absolute;left:0;top:0" width="327" height="184" viewBox="0 0 327 184" role="img" aria-label="Hexagon collage of detailed cars: red coupe, wheel with yellow caliper, dark rear light bar, black interior">
    <defs>
      <linearGradient id="cRed" x1="0" y1="0" x2="1" y2="1"><stop offset="0" stop-color="#3a3d44"/><stop offset=".5" stop-color="#b3181e"/><stop offset="1" stop-color="#2a2b2e"/></linearGradient>
      <linearGradient id="cDark" x1="0" y1="0" x2="1" y2="1"><stop offset="0" stop-color="#55575c"/><stop offset="1" stop-color="#1d1d20"/></linearGradient>
      <linearGradient id="cRear" x1="0" y1="0" x2="0" y2="1"><stop offset="0" stop-color="#4a4b50"/><stop offset=".55" stop-color="#2a2a2d"/><stop offset=".6" stop-color="#a3161c"/><stop offset="1" stop-color="#1b1b1d"/></linearGradient>
    </defs>
    <polygon points="195,3 250,3 273,45 250,87 195,87 172,45" fill="url(#cRed)"/>
    <polygon points="259,0 327,0 327,40 282,40" fill="url(#cDark)"/>
    <polygon points="260,48 327,48 327,135 272,135 252,92 282,48" fill="url(#cDark)"/>
    <polygon points="195,93 250,93 273,135 250,184 195,184 172,135" fill="url(#cRear)"/>
    <polygon points="278,142 327,142 327,184 256,184" fill="url(#cDark)"/>
  </svg>
  <div class="brand" style="left:25px;top:28px">Vantrel Detailing</div>
  <h2 class="title" style="top:45px">Contact <em>Us</em></h2>
  <p class="lede" style="top:66px;width:108px">Lorem ipsum dolor sit amet, consectetur adipiscing elit sed do eiusmod tempor incididunt ut labore et dolore magna aliqua. Ut enim ad minim veniam</p>
  <div class="contact-label" style="top:104px">Address</div>
  <div class="contact-label" style="top:121px">Email</div>
  <div class="contact-label" style="top:138px">Website</div>
  <span class="social" style="left:26px"></span>
  <span class="social" style="left:36px"></span>
  <span class="social" style="left:46px"></span>
  <div class="footer" style="right:160px"><span></span><span></span></div>
  <div class="page-no">08</div>
</section>

<!-- Short Break slide -->
<section class="slide" style="left:790px;top:454px">
  <div class="photo" role="img" aria-label="White brake caliper and carbon ceramic disc on a wheel hub" style="left:215px;top:0;width:112px;height:184px;background:radial-gradient(ellipse at 40% 55%,#e5e5e7 0,#8d8e92 35%,#3c3d41 70%,#1f1f21)"></div>
  <div style="position:absolute;left:42px;top:32px;width:128px;height:80px;background:linear-gradient(180deg,#2e2e31,#121214)"></div>
  <div class="brand" style="left:60px;top:95px;font-size:11px;gap:4px">Vantrel Detailing</div>
  <h2 class="title" style="left:58px;top:128px">Short <em>Break</em></h2>
</section>

<!-- Thank You slide -->
<section class="slide" style="left:64px;top:654px">
  <div style="position:absolute;left:0;top:0;width:218px;height:184px;background:linear-gradient(180deg,#3a3a3d 0,#1d1d1f 60%,#111113)"></div>
  <div class="brand" style="left:34px;top:130px;font-size:17px;gap:5px">Vantrel Detailing</div>
  <h2 class="title" style="left:205px;top:83px">THANK <em>YOU</em></h2>
</section>

<h2 class="section-heading">Alternative Content Slides</h2>

<!-- Alternative content slide A -->
<section class="slide" style="left:69px;top:955px;width:325px;height:182px">
  <div class="brand" style="left:283px;top:18px">Vantrel Detailing</div>
  <h2 class="title" style="top:31px">GOALS &amp; <em>OBJECTIVES</em></h2>
  <div style="position:absolute;left:25px;top:62px;width:135px">
    <div class="goal"><h4>Revenue Growth</h4><p>Grow repeat bookings and lift monthly revenue through loyal returning clients.</p></div>
    <div class="goal"><h4>Profit Margins</h4><p>Cut admin hours and missed follow-ups so each job keeps more margin.</p></div>
    <div class="goal"><h4>Sustainability</h4><p>Build steady processes the team can run without the owner on site.</p></div>
    <div class="goal"><h4>Return On Investment</h4><p>Recover the system cost within the first year of retained customers.</p></div>
  </div>
  <div style="position:absolute;left:172px;top:62px;width:135px">
    <div class="goal"><h4>Revenue Growth</h4><p>Grow repeat bookings and lift monthly revenue through loyal returning clients.</p></div>
    <div class="goal"><h4>Profit Margins</h4><p>Cut admin hours and missed follow-ups so each job keeps more margin.</p></div>
    <div class="goal"><h4>Sustainability</h4><p>Build steady processes the team can run without the owner on site.</p></div>
    <div class="goal"><h4>Return On Investment</h4><p>Recover the system cost within the first year of retained customers.</p></div>
  </div>
  <div class="footer" style="top:163px"><span>Automotive Detailing, <span class="accent">CRM System</span></span><span>03</span></div>
</section>

<!-- Alternative content slide B -->
<section class="slide" style="left:429px;top:955px">
  <div class="photo" role="img" aria-label="White sedan parked inside a detailing studio with roller door and branded wall" style="left:158px;top:0;width:169px;height:184px;background:linear-gradient(180deg,#5a5d62 0,#3a3c40 45%,#8c8e92 70%,#6b6d70 100%)"></div>
  <div class="brand" style="left:25px;top:28px">Vantrel Detailing</div>
  <h2 class="title" style="top:38px">GOALS &amp; <em>OBJECTIVES</em></h2>
  <div style="position:absolute;left:25px;top:68px;width:125px">
    <div class="goal"><h4>Revenue Growth</h4><p>Grow repeat bookings and lift monthly revenue through loyal returning clients.</p></div>
    <div class="goal"><h4>Profit Margins</h4><p>Cut admin hours and missed follow-ups so each job keeps more margin.</p></div>
    <div class="goal"><h4>Sustainability</h4><p>Build steady processes the team can run without the owner on site.</p></div>
    <div class="goal"><h4>Return On Investment</h4><p>Recover the system cost within the first year of retained customers.</p></div>
  </div>
  <div class="footer" style="top:167px"><span>Automotive Detailing, <span class="accent">CRM System</span></span><span>03</span></div>
</section>

</body>
</html>
```